Redesign My Travel Voucher Coupons-Please redesign the flyers I have attached to this brief.

These designs will be catered towards like travel agency vacation stays...luxury resort stays, hotel and airfare getaways, etc. so must have a travel theme but more importantly professional trustworthy appeal...

Please redesign the flyers I have attached to this brief.

I have attached my existing designs. Please use all existing content and elements exactly but make the design much better...also, please keep in mind that these would be full color and printer friendly...

Target Market(s)

Consumers. People receive these vouchers from businesses that run marketing promotions and contests and giveaways. So the look and feel must feel professional and trustworthy but not cheesy and fake.

Industry/Entity Type

Hotel

Requirements
Must have
• Please use all existing content and elements exactly but make the design much better...also, please keep in mind that these would be full color and printer friendly...

MUST HAVE ALL EXISTING CONTENT EXACT NO EXCEPTIONS
Nice to have
• These designs will be catered towards like travel agency vacation stays...luxury resort stays, hotel and airfare getaways, etc. so must have a travel theme but more importantly professional trustworthy appeal...

Should not have

```html
<!DOCTYPE html>
<html lang="en">
<head>
<meta charset="utf-8">
<title>Enjoy Travel Certificates</title>
<link rel="stylesheet" href="https://fonts.googleapis.com/css2?family=Comfortaa:wght@500;700&family=Great+Vibes&family=Montserrat:wght@500;700;800&family=Raleway:ital,wght@0,400;0,500;1,400&display=swap">
<style>
  :root {
    --page: #f3f1ec;
    --paper: #fcfaf3;
    --ink: #3a3a3a;
    --ink-soft: #555555;
    --white: #ffffff;
    --sun: #f6d35b;
    --sun-deep: #f7bf45;
    --teal: #3aa4a6;
    --teal-deep: #2a7f86;
    --navy: #1f2b4a;
  }
  * { box-sizing: border-box; margin: 0; padding: 0; }
  html, body { width: 1200px; height: 3000px; overflow: hidden; background: var(--page); }
  body { position: relative; font-family: "Raleway", Arial, sans-serif; color: var(--ink); }

  /* flyer frame */
  .flyer {
    position: absolute; width: 771px; height: 998px; overflow: hidden;
    background: var(--paper); box-shadow: 0 1px 6px rgba(0,0,0,.08);
    --panel-top: 290px; --panel-h: 210px; --cols-top: 313px; --how-top: 532px; --rev-top: 727px;
  }
  .flyer--main { left: 213px; top: 231px; }
  .flyer--mini { transform: scale(0.476); transform-origin: 0 0; }
  .pos-l { left: 213px; } .pos-r { left: 617px; }
  .row-1 { top: 1268px; } .row-2 { top: 1781px; } .row-3 { top: 2296px; }

  /* hero */
  .hero { position: absolute; left: 0; top: 0; width: 100%; height: 500px; }
  .panel { position: absolute; left: 0; top: var(--panel-top); width: 100%; height: var(--panel-h); background: var(--panel); opacity: .94; }

  .brand-word {
    position: absolute; left: 72px; top: 92px;
    font-family: "Montserrat", sans-serif; font-weight: 800; font-size: 86px; line-height: 86px;
    color: var(--brand); letter-spacing: 1px;
  }
  .offer-band {
    position: absolute; left: 0; top: 180px; width: 367px; height: 34px;
    background: var(--band); color: var(--band-text);
    font-family: "Comfortaa", sans-serif; font-weight: 500; font-size: 21px;
    line-height: 34px; padding-left: 72px; white-space: nowrap;
  }
  .offer-band--tall { height: 68px; line-height: 30px; padding-top: 4px; white-space: normal; }
  .offer-sub {
    position: absolute; left: 72px; top: 222px; width: 300px;
    font-family: "Comfortaa", sans-serif; font-weight: 700; font-size: 17px; line-height: 1.2;
    color: var(--sub);
  }

  .block-title {
    font-family: "Montserrat", sans-serif; font-weight: 800; font-size: 13px;
    text-transform: uppercase; margin-bottom: 5px; letter-spacing: .2px;
  }
  .col-left { position: absolute; left: 72px; top: var(--cols-top); width: 320px; color: var(--white); }
  .col-right { position: absolute; left: 415px; top: var(--cols-top); width: 300px; color: var(--white); }
  .copy { font-size: 12px; line-height: 15.5px; }
  .feature-list { list-style: none; font-family: "Montserrat", sans-serif; font-weight: 700; font-size: 10px; line-height: 13px; text-transform: uppercase; }
  .feature-list li { padding-left: 9px; text-indent: -9px; }
  .feature-list li::before { content: "\2022  "; }

  .how { position: absolute; left: 72px; top: var(--how-top); width: 627px; color: var(--ink); }
  .how .copy { font-size: 12px; line-height: 16px; color: var(--ink-soft); }
  .reviews { position: absolute; right: 72px; top: var(--rev-top); width: 620px; text-align: right; color: var(--ink); }
  .reviews q { display: block; font-style: italic; font-size: 11px; line-height: 1.4; color: var(--ink-soft); quotes: "\201C" "\201D"; }
  .reviews cite { display: block; font-style: italic; font-size: 11px; margin-top: 8px; color: var(--ink-soft); }

  /* footer */
  .footer {
    position: absolute; left: 0; bottom: 0; width: 100%; height: 127px;
    background: linear-gradient(90deg, var(--foot-a) 0%, var(--foot-b) 72%);
  }
  .footer-contact { position: absolute; left: 72px; top: 12px; width: 160px; color: var(--foot-ink); }
  .compliments { font-family: "Great Vibes", cursive; font-size: 19px; color: var(--foot-accent); margin-left: 14px; line-height: 1.1; }
  .contact-name { font-family: "Montserrat", sans-serif; font-weight: 700; font-size: 13px; }
  .contact-line { font-family: "Montserrat", sans-serif; font-weight: 500; font-size: 10.5px; line-height: 1.3; }
  .issuer { display: flex; align-items: center; gap: 5px; margin-top: 6px; font-family: "Montserrat", sans-serif; font-weight: 700; font-size: 11px; color: var(--foot-accent); }
  .issuer-mark { width: 10px; height: 10px; background: var(--foot-accent); }
  .footer-offer { position: absolute; left: 234px; top: 24px; width: 310px; color: var(--foot-accent); font-size: 12.5px; line-height: 1.3; text-transform: uppercase; }
  .footer-offer .terms { text-transform: none; font-size: 11px; margin-top: 2px; }
  .footer-cert { position: absolute; right: 0; top: 0; width: 212px; height: 100%; background: var(--cert); color: var(--white); padding: 24px 0 0 50px; font-size: 13.5px; line-height: 1.35; }

  /* main flyer */
  .flyer--main {
    --brand: var(--sun); --band: var(--sun); --band-text: var(--teal-deep); --sub: var(--navy);
    --foot-a: var(--paper); --foot-b: var(--sun-deep); --foot-ink: var(--teal-deep); --foot-accent: var(--teal);
    --cert: var(--teal);
  }
  .flyer--main .hero { background: linear-gradient(180deg, #4fbde3 0%, #7fd0ec 22%, #bfe6f0 36%, #5cb6c8 40%, #7ccbd2 50%, #a9dcdc 58%, #6fbcbf 70%, #3f9ea3 100%); }
  .flyer--main .panel { background: linear-gradient(180deg, rgba(58,164,166,0) 0%, rgba(52,150,154,.72) 30%, rgba(44,136,142,.88) 100%); opacity: 1; }
  .flyer--main .offer-band { width: 384px; font-size: 25px; line-height: 35px; height: 35px; padding-left: 92px; }
  .flyer--main .offer-sub { top: 224px; width: 380px; font-size: 17.5px; }
  .flyer--main .col-left { width: 318px; }
  .flyer--main .col-left .copy { font-size: 13.5px; line-height: 16.4px; }
  .flyer--main .col-right { left: 420px; width: 300px; }
  .flyer--main .feature-list { font-size: 11.5px; line-height: 15px; }
  .flyer--main .how .copy { font-size: 13px; line-height: 16.4px; }
  .flyer--main .reviews q, .flyer--main .reviews cite { font-size: 12.5px; line-height: 17.5px; }

  /* themes */
  .theme-resort { --brand: #a4472d; --band: #a4472d; --band-text: #fff; --sub: #4a2a22; --panel: #a6492f;
    --foot-a: #f2ebe2; --foot-b: #d9c6b4; --foot-ink: #4a3a33; --foot-accent: #6a4a3e; --cert: #a4472d;
    --panel-top: 286px; --panel-h: 208px; --cols-top: 300px; --how-top: 538px; --rev-top: 734px; }
  .theme-resort .hero { background: linear-gradient(100deg, #eef0ee 0%, #dfe6e8 30%, #8fb7d3 48%, #5a9cc8 60%, #a9cde0 75%, #e6ecee 100%); }
  .theme-cruise { --brand: #27355f; --band: #2b3a66; --band-text: #fff; --sub: #fff; --panel: #2f5f92;
    --foot-a: #eef5fb; --foot-b: #bfdcf3; --foot-ink: #2b3a66; --foot-accent: #2b3a66; --cert: #4a4c7e;
    --panel-top: 328px; --panel-h: 166px; --cols-top: 352px; --how-top: 531px; --rev-top: 760px; }
  .theme-cruise .hero { background: linear-gradient(180deg, #e4eef6 0%, #c6dcec 30%, #9cc1dd 50%, #5f92c0 68%, #3d74a8 100%); }
  .theme-hotel { --brand: #4a2a3e; --band: #4a2a3e; --band-text: #fff; --sub: #2b1f2a; --panel: #6d5868;
    --foot-a: #f4f0f1; --foot-b: #cfc2c8; --foot-ink: #4a2a3e; --foot-accent: #4a2a3e; --cert: #5a4658;
    --panel-top: 419px; --panel-h: 232px; --cols-top: 443px; --how-top: 656px; --rev-top: 761px; }
  .theme-hotel .hero { background: linear-gradient(180deg, #f1f6f8 0%, #d9ecf1 30%, #8fd6dc 48%, #4cc3c6 62%, #35aab0 78%, #7fc9c9 100%); }
  .theme-dining { --brand: #5a1a1e; --band: #5a1a1e; --band-text: #fff; --sub: #2e1a1a; --panel: #7b2e2b;
    --foot-a: #f7f2ec; --foot-b: #eee2d8; --foot-ink: #5a1a1e; --foot-accent: #8a2a2a; --cert: #7a3a3a;
    --panel-top: 389px; --panel-h: 220px; --cols-top: 401px; --how-top: 614px; --rev-top: 761px; }
  .theme-dining .hero { background: linear-gradient(180deg, #f4efe8 0%, #e6d6c4 30%, #c8a283 55%, #a86e4f 80%, #8b4f3a 100%); }
  .theme-paris { --brand: #f08a7a; --band: #f08a7a; --band-text: #fff; --sub: #2b3a66; --panel: #2b3a66;
    --foot-a: #5a6e98; --foot-b: #8aa6c8; --foot-ink: #fff; --foot-accent: #fff; --cert: #f29a8a;
    --panel-top: 384px; --panel-h: 206px; --cols-top: 396px; --how-top: 629px; --rev-top: 756px; }
  .theme-paris .hero { background: linear-gradient(180deg, #eef2f8 0%, #d6e1ee 30%, #aebfd8 55%, #7f9cc2 80%, #5d7aa6 100%); }
  .theme-mexico { --brand: #f0622e; --band: #f0622e; --band-text: #fff; --sub: #1f2b4a; --panel: #2a6b8d;
    --foot-a: #4c88a8; --foot-b: #9cc8e0; --foot-ink: #fff; --foot-accent: #fff; --cert: #f0622e;
    --panel-top: 291px; --panel-h: 208px; --cols-top: 308px; --how-top: 548px; --rev-top: 756px; }
  .theme-mexico .hero { background: linear-gradient(180deg, #cdb9d2 0%, #b7c4dc 22%, #9ecbe0 40%, #4ea6c8 58%, #2f86ad 78%, #2a6b8d 100%); }

  .theme-cruise .col-left { width: 318px; }
  .theme-cruise .col-second { left: 397px; top: 372px; width: 313px; }
  .theme-cruise .how { width: 318px; }
  .theme-cruise .how-features { position: absolute; left: 397px; top: var(--how-top); width: 313px; color: var(--ink); }
</style>
</head>
<body>

<section class="flyer flyer--main">
  <div class="hero" role="img" aria-label="Photo of an infinity pool terrace overlooking a turquoise sea, with a rolled towel and an open book"></div>
  <div class="panel"></div>
  <h1 class="brand-word">ENJOY</h1>
  <div class="offer-band">A 2 Night Hotel Stay</div>
  <p class="offer-sub">3 + &nbsp;Star Hotel Accommodations in the City of Your Choice of over 50 of the Most Popular Destinations Available!</p>
  <div class="col-left">
    <h2 class="block-title">Exclusively for:</h2>
    <p class="copy">There is no doubt that everyone wishes they can take a much needed vacation to just relax and unwind while having fun at the same time! Enjoy two nights of hotel accommdations in the city of your choice of over 50 of the hottest, most desired vacation spots around the country. Thanks to the business you received this certificate from, now you can enjoy a nice little mini vacation you deserve!</p>
  </div>
  <div class="col-right">
    <h2 class="block-title">Features:</h2>
    <ul class="feature-list">
      <li>Travel 7 days a week</li>
      <li>Good for two adults &amp; two children</li>
      <li>Multiple travel date requests allowed</li>
      <li>No timeshare no sales presentation</li>
      <li>Your choice of over 50 luxury destinations</li>
      <li>Pay just the taxes &amp; fees</li>
      <li>Fully transferable to another person</li>
      <li>24 months to complete travel after redemption</li>
    </ul>
  </div>
  <div class="how">
    <h2 class="block-title">How can we do this:</h2>
    <p class="copy">We contract with the world leading hotel chains and resorts to help them fill their otherwise empty rooms. We help fill empty rooms which the hotels, resorts and cruise lines turn into additional revenue from other areas of their property and future bookings.<br>Hotels rarely experience full occupancy, yet they remain open, providing rooms and services at fixed costs. So when hotels give out their rooms by partnering with marketing companies like us, they might miss out on the room fee, but they already didn't have that in the first place, at least now they have the opportunity to gain a customer for their in-house restaurants, room service, their casinos, an extra day stay, future bookings, etc.</p>
  </div>
  <div class="reviews">
    <h2 class="block-title">What others say</h2>
    <q>Being able to stay right on the strip in Las Vegas was great. I love that we were able to walk around to all the sites and attractions. The fountains at the Lumière were AMAZING! The Gondola ride at the Canal Palace was very nice. I LOVED the atmosphere and the food. The whole experience was awesome. THANK YOU!</q>
    <cite>Karen M. San Diego, CA</cite>
  </div>
  <footer class="footer">
    <div class="footer-contact">
      <div class="compliments">Compliments of</div>
      <div class="contact-name">Dana Whitfield</div>
      <div class="contact-line">555-014-2290</div>
      <div class="contact-line">GrowYourGuests.com</div>
      <div class="issuer"><span class="issuer-mark"></span>Brightway Rewards</div>
    </div>
    <div class="footer-offer">View all the details of this special offer and redeem online at:<br>www.getawayperks.com<div class="terms">*Terms and Conditions apply, see website for details.</div></div>
    <div class="footer-cert">Certificate ID:<br>107083-11266<br>Expires:<br>11/07/2021</div>
  </footer>
</section>

<section class="flyer flyer--mini pos-l row-1 theme-resort">
  <div class="hero" role="img" aria-label="Photo of a white colonnade terrace with a chandelier opening onto a blue sea"></div>
  <div class="panel"></div>
  <h1 class="brand-word">ENJOY</h1>
  <div class="offer-band">7 Nights in a luxury Resort</div>
  <p class="offer-sub">Choose Resort from over 3500 Locations Worldwide</p>
  <div class="col-left">
    <h2 class="block-title">Exclusively for:</h2>
    <p class="copy">Congratulations, you are the recipient of 7 nights luxury resort accommodations. This special offer is good for two adults. Two adults 7 nights of luxurious resort accommodations in one of 3500 available resorts worldwide. Choose from thousands of U.S destinations and hundreds of international destinations. Lots of local drive-to resorts as well as exotic fly-to destinations.</p>
  </div>
  <div class="col-right">
    <h2 class="block-title">Features:</h2>
    <ul class="feature-list">
      <li>Travel 7 days a week</li>
      <li>Over 3500 locations worldwide to choose from</li>
      <li>Pay just taxes &amp; fees</li>
      <li>Redeem now, travel later</li>
      <li>No blackout dates</li>
      <li>Good for two adults &amp; two guests</li>
      <li>Fully transferable to another person</li>
      <li>You have up to 24 months to complete the travel offer</li>
    </ul>
  </div>
  <div class="how">
    <h2 class="block-title">How can we do this:</h2>
    <p class="copy">We contract with the world leading hotel chains and resorts to help them fill their otherwise empty rooms. We help fill empty rooms which the hotels, resorts and cruise lines turn into additional revenue from other areas of their property and future bookings.<br>Hotels rarely experience full occupancy, yet they remain open, providing rooms and services at fixed costs. So when hotels give out their rooms by partnering with marketing companies like us, they might miss out on the room fee, but they already didn't have that in the first place, at least now they have the opportunity to gain a customer for their in-house restaurants, room service, their casinos, an extra day stay, future bookings, etc.</p>
  </div>
  <div class="reviews">
    <h2 class="block-title">What others say</h2>
    <q>We won this trip at a raffle at our annual golf show and were able to use it for our honeymoon! We were able to go right away after our wedding. The resort was amazing. The pools, the beach, the whole deal. The real deal. Thank you!</q>
    <cite>Mark T. Atlanta, Georgia</cite>
  </div>
  <footer class="footer">
    <div class="footer-contact">
      <div class="compliments">Compliments of</div>
      <div class="contact-name">Dana Whitfield</div>
      <div class="contact-line">555-014-2290</div>
      <div class="contact-line">GrowYourGuests.com</div>
      <div class="issuer"><span class="issuer-mark"></span>Brightway Rewards</div>
    </div>
    <div class="footer-offer">View all the details of this special offer and redeem online at<br>www.getawayperks.com<div class="terms">*Terms and Conditions apply, see website for details.</div></div>
    <div class="footer-cert">Certificate ID:<br>107083-11268<br>Expires:<br>11/07/2021</div>
  </footer>
</section>

<section class="flyer flyer--mini pos-r row-1 theme-cruise">
  <div class="hero" role="img" aria-label="Photo of a white cruise ship sailing on a calm blue sea"></div>
  <div class="panel"></div>
  <h1 class="brand-word">ENJOY</h1>
  <div class="offer-band offer-band--tall">A 4 Night Luxury Cruise<br>Getaway</div>
  <div class="col-left">
    <h2 class="block-title">Exclusively for:</h2>
    <p class="copy">Congratulations, you are the lucky recipient of a 5 day / 4 night Cruise aboard choice of: Azure Line, Coral Crown Cruises, Northstar Cruise Line, or Regal Seas. There are 3 itineraries w/ ports of departure including: Miami to Cozumel, Port Canaveral to Nassau, or LA to Ensenada, Mexico.</p>
  </div>
  <div class="col-left col-second">
    <p class="copy">All cruises include unlimited access to the on-board buffets for breakfast, lunch and dinner. Vegas style entertainment and use of all on-board facilities. You simply pay taxes and port fees. Have the time of your life while enjoying the luxuries of a cruise vacation!</p>
  </div>
  <div class="how">
    <h2 class="block-title">How can we do this:</h2>
    <p class="copy">We contract with world leading cruise lines to help them fill their otherwise empty rooms. The cruise lines now gain a new customer for their in-house restaurants, room service, the casino, spa and even future bookings. They know that if they show you a good time, you will probably tell your friends and family about the great time you had and may even book with them on a future cruise, but this time as a regular paying customer.</p>
  </div>
  <div class="how-features">
    <h2 class="block-title">Features:</h2>
    <ul class="feature-list">
      <li>Phone bookings with a live agent</li>
      <li>Sailing from: Miami, Port Canaveral or Los Angeles</li>
      <li>Fully transferable to another person</li>
      <li>You will have 24 months to complete travel offer</li>
      <li>Sail to: Cozumel, Nassau Bahamas or Ensenada</li>
      <li>Pay just taxes &amp; fees</li>
      <li>Redeem now, travel later</li>
      <li>No timeshare or sales presentations, guaranteed!</li>
    </ul>
  </div>
  <div class="reviews">
    <h2 class="block-title">What others say</h2>
    <q>The food was delicious in the buffet and the restaurant that was included in our ticket had delicious appetizers, entrees and desserts to choose from. The room was very clean and everything worked fine.</q>
    <cite>Tessa L. Kansas City, MO</cite>
  </div>
  <footer class="footer">
    <div class="footer-contact">
      <div class="compliments">Compliments of</div>
      <div class="contact-name">Dana Whitfield</div>
      <div class="contact-line">555-014-2290</div>
      <div class="contact-line">GrowYourGuests.com</div>
      <div class="issuer"><span class="issuer-mark"></span>Brightway Rewards</div>
    </div>
    <div class="footer-offer">View all the details of this special offer and redeem online at<br>www.getawayperks.com<div class="terms">*Terms and Conditions apply, see website for details.</div></div>
    <div class="footer-cert">Certificate ID:<br>107083-11269<br>Expires:<br>11/07/2021</div>
  </footer>
</section>

<section class="flyer flyer--mini pos-l row-2 theme-hotel">
  <div class="hero" role="img" aria-label="Photo of overwater bungalows on a wooden walkway above a turquoise lagoon"></div>
  <div class="panel"></div>
  <h1 class="brand-word">ENJOY</h1>
  <div class="offer-band">$500 OFF</div>
  <p class="offer-sub">Get $500 off at over 400,000 Hotel&amp;Resort Properties Worldwide!</p>
  <div class="col-left">
    <h2 class="block-title">Exclusively for:</h2>
    <p class="copy">The best discounts available in travel. Web-based technologies focused on having the absolute lowest prices on hotels, resorts and other travel products. Proprietary technology has created an all-encompassing, easy-to-use web platform that brings unparalleled pricing to all types of travelers. Superior customer service and online transparency allows for credibility and consistency to customers and site users, making it the fastest growing travel website aggregator.</p>
  </div>
  <div class="col-right">
    <h2 class="block-title">Features:</h2>
    <ul class="feature-list">
      <li>Save up to 50% on travel</li>
      <li>No blackout dates or restrictions</li>
      <li>400,000 top brand hotels &amp; resorts</li>
      <li>12 months to book travel</li>
      <li>Thousands of activities</li>
      <li>8,000 rental car locations</li>
      <li>Easy online bookings</li>
      <li>Redeem now, travel later</li>
      <li>Fully transferable to another person</li>
      <li>Millions of happy travelers</li>
    </ul>
  </div>
  <div class="how">
    <h2 class="block-title">How can we do this:</h2>
    <p class="copy">Redeem your certificate to activate your account. Once activated you can login to your personal travel booking portal anytime you wish to check travel availability and book travel. Anytime you book travel you can use your travel dollars towards the booking to get your instant discount.<br>It really is that easy!</p>
  </div>
  <div class="reviews">
    <h2 class="block-title">What others say</h2>
    <q>I saved a lot of money using my savings dollars. I get $150 every month for paying my insurance policy on time. I recently booked a 10 day vacation for Hawaii in 2021 and I saved over $1000!</q>
    <cite>Tessa L. Kansas City, MO</cite>
  </div>
  <footer class="footer">
    <div class="footer-contact">
      <div class="compliments">Compliments of</div>
      <div class="contact-name">Dana Whitfield</div>
      <div class="contact-line">555-014-2290</div>
      <div class="contact-line">GrowYourGuests.com</div>
      <div class="issuer"><span class="issuer-mark"></span>Brightway Rewards</div>
    </div>
    <div class="footer-offer">View all the details of this special offer and redeem online at<br>www.getawayperks.com<div class="terms">*Terms and Conditions apply, see website for details.</div></div>
    <div class="footer-cert">Certificate ID:<br>107083-11264<br>Expires:<br>11/07/2021</div>
  </footer>
</section>

<section class="flyer flyer--mini pos-r row-2 theme-dining">
  <div class="hero" role="img" aria-label="Photo of friends sharing a meal at a bright restaurant table"></div>
  <div class="panel"></div>
  <h1 class="brand-word">ENJOY</h1>
  <div class="offer-band">$500 OFF</div>
  <p class="offer-sub">$500 off at Thousands of Participating Restaurants</p>
  <div class="col-left">
    <h2 class="block-title">Exclusively for:</h2>
    <p class="copy">Congratulations, you are the recipient of $500 worth of restaurant cash. For the next 20 months you will receive a $25 Restaurant Cash that you can use at your choice out of thousands of participating restaurants nationwide. In addition, you will also have access to an unlimited amount of the latest and greatest fast food and restaurant coupons that you can use to receive discounts at your favorite food spots anytime you want.</p>
  </div>
  <div class="col-right">
    <h2 class="block-title">Features:</h2>
    <ul class="feature-list">
      <li>Twenty $25 off restaurant cash vouchers</li>
      <li>Access to latest &amp; greatest fast food coupons</li>
      <li>Thousands of new restaurants added monthly</li>
      <li>Local &amp; nationally known restaurants</li>
      <li>18,000+ restaurants participate nationwide</li>
      <li>Discover your new favorite restaurants</li>
      <li>Up to 50% off your dining bill</li>
      <li>So many options, tons of savings</li>
    </ul>
  </div>
  <div class="how">
    <h2 class="block-title">How can we do this:</h2>
    <p class="copy">We drive a ton of new diners to thousands of restaurants nationwide to fill their empty tables. Majority of customers that we send to these restaurants spend around $66 with a $25 gift certificate. The whole magic of these promotions is for your customer to enjoy a new restaurant that they otherwise would not have visited and the restaurant knows if the customer has a great meal at a great deal they'll be more inclined to visit again as a regular paying customer in the future. It is all about building brand awareness and customer loyalty for the restaurants involved.</p>
  </div>
  <div class="reviews">
    <h2 class="block-title">What others say</h2>
    <q>I used my $25 at a great Italian restaurant that I have always wanted to try but never got to it. Thanks to this certificate I was able to finally try them. Very glad I did because now they are my favorite Italian spot in San Diego.</q>
    <cite>Renee D. San Diego, CA</cite>
  </div>
  <footer class="footer">
    <div class="footer-contact">
      <div class="compliments">Compliments of</div>
      <div class="contact-name">Dana Whitfield</div>
      <div class="contact-line">555-014-2290</div>
      <div class="contact-line">GrowYourGuests.com</div>
      <div class="issuer"><span class="issuer-mark"></span>Brightway Rewards</div>
    </div>
    <div class="footer-offer">View all the details of this special offer<br>www.getawayperks.com<div class="terms">*Terms and Conditions apply, see website for details.</div></div>
    <div class="footer-cert">Certificate ID:<br>107083-11265<br>Expires:<br>11/07/2021</div>
  </footer>
</section>

<section class="flyer flyer--mini pos-l row-3 theme-paris">
  <div class="hero" role="img" aria-label="Photo of a traveler with a backpack looking toward a tall iron tower in a misty city"></div>
  <div class="panel"></div>
  <h1 class="brand-word">ENJOY</h1>
  <div class="offer-band">$500 OFF</div>
  <p class="offer-sub">Get $500 off at over 400,000 Hotels&amp;Resort Properties Worldwide</p>
  <div class="col-left">
    <h2 class="block-title">Exclusively for:</h2>
    <p class="copy">The best discounts available in travel. Web-based technologies focused on having the absolute lowest prices on hotels, resorts and other travel products. Proprietary technology has created an all-encompassing, easy-to-use web platform that brings unparalleled pricing to all types of travelers. Superior customer service and online transparency allows for credibility and consistency to customers and site users, making it the fastest growing travel website aggregator.</p>
  </div>
  <div class="col-right">
    <h2 class="block-title">Features:</h2>
    <ul class="feature-list">
      <li>Save up to 50% on travel</li>
      <li>No blackout dates or restrictions</li>
      <li>400,000 top brand hotels &amp; resorts</li>
      <li>12 months to book travel</li>
      <li>Thousands of activities</li>
      <li>8,000 rental car locations</li>
      <li>Easy online bookings</li>
      <li>Redeem now, travel later</li>
      <li>Fully transferable to another person</li>
      <li>Millions of happy travelers</li>
    </ul>
  </div>
  <div class="how">
    <h2 class="block-title">How can we do this:</h2>
    <p class="copy">Redeem your certificate to activate your account. Once activated you can login to your personal travel booking portal anytime you wish to check travel availability and book travel. Anytime you book travel you can use your travel dollars towards the booking to get your instant discount.<br>It really is that easy</p>
  </div>
  <div class="reviews">
    <h2 class="block-title">What others say</h2>
    <q>I saved a lot of money using my savings dollars. I get $100 every month for paying my insurance policy on time. I recently booked a 10-day vacation for Hawaii in 2021 and I saved over $1200!</q>
    <cite>Tessa L. Kansas City, MO</cite>
  </div>
  <footer class="footer">
    <div class="footer-contact">
      <div class="compliments">Compliments of</div>
      <div class="contact-name">Dana Whitfield</div>
      <div class="contact-line">555-014-2290</div>
      <div class="contact-line">GrowYourGuests.com</div>
      <div class="issuer"><span class="issuer-mark"></span>Brightway Rewards</div>
    </div>
    <div class="footer-offer">View all the details of this special offer and redeem online at<br>www.getawayperks.com<div class="terms">*Terms and Conditions apply, see website for details.</div></div>
    <div class="footer-cert">Certificate ID:<br>107083-11264<br>Expires:<br>11/07/2021</div>
  </footer>
</section>

<section class="flyer flyer--mini pos-r row-3 theme-mexico">
  <div class="hero" role="img" aria-label="Aerial photo of a beach resort coastline with turquoise water at dusk"></div>
  <div class="panel"></div>
  <h1 class="brand-word">ENJOY</h1>
  <div class="offer-band">Mexico Resort Luxury</div>
  <p class="offer-sub">4 Night Mexico Beach Resort Getaway</p>
  <div class="col-left">
    <h2 class="block-title">Exclusively for:</h2>
    <p class="copy">Congratulations, you have been rewarded with 4 nights of Luxurious Beach Resort Accommodations in your choice of either Mazatlan, Acapulco, Puerto Penasco, Puerta Vallarta, Cancun or Nuevo Vallarta, Mexico! Have the time of your life, redeem your certificate now and start planning your next Luxurious Mexico Beach Vacation today!<br>This offer includes two adults!</p>
  </div>
  <div class="col-right">
    <h2 class="block-title">Features:</h2>
    <ul class="feature-list">
      <li>4-5 star luxury beach destinations</li>
      <li>Six Mexico destinations</li>
      <li>Just pay taxes &amp; fees</li>
      <li>You will have 24 months to complete travel</li>
      <li>Mayan properties</li>
      <li>Transferable to another person</li>
      <li>Redeem now, travel later</li>
      <li>No timeshare or sales presentations, guaranteed</li>
    </ul>
  </div>
  <div class="how">
    <h2 class="block-title">How can we do this:</h2>
    <p class="copy">We contract with the world leading hotel chains and resorts to help them fill their otherwise empty rooms. We help fill empty rooms which the hotels, resorts and cruise lines turn into additional revenue from other areas of their property and future bookings.<br>Hotels rarely experience full occupancy, yet they remain open, providing rooms and services at fixed costs. So when hotels give out their rooms by partnering with marketing companies like us, they might miss out on the room fee, but they already didn't have that in the first place, at least now they have the opportunity to gain a customer for their in-house restaurants, room service, their casinos, an extra day stay, future bookings, etc.</p>
  </div>
  <div class="reviews">
    <h2 class="block-title">What others say</h2>
    <q>Great time to get away. The steakhouse had great dessert. Resort was in a great location, right on the beach in Cabo. Needless to say the beaches were absolutely BEAUTIFUL!</q>
    <cite>Paula K. Boston, MA</cite>
  </div>
  <footer class="footer">
    <div class="footer-contact">
      <div class="compliments">Compliments of</div>
      <div class="contact-name">Dana Whitfield</div>
      <div class="contact-line">555-014-2290</div>
      <div class="contact-line">GrowYourGuests.com</div>
      <div class="issuer"><span class="issuer-mark"></span>Brightway Rewards</div>
    </div>
    <div class="footer-offer">View all the details of this special offer and redeem online at<br>www.getawayperks.com<div class="terms">*Terms and Conditions apply, see website for details.</div></div>
    <div class="footer-cert">Certificate ID:<br>107083-11267<br>Expires:<br>11/07/2021</div>
  </footer>
</section>

</body>
</html>
```